Bride Basecamp

I am looking for a design for http://www.bridebasecamp.co.uk/ its a joomla site and I am going to set up with the same mods as our stag version http://www.groomsnightout.co.uk/ you will see on groomsnight how all the menus look and are positioned. Here is an example of a activity page http://www.groomsnightout.co.uk/activity/white-water-rafting-in-perthshire.html which comes from Kiva.

The design needs to be built for responsive layout. The brand look and feel needs to be 100% for the female market.

We can accept the design in photoshop or something similar

Please ask questions if you require more information.

some examples of hen sites

http://www.girlsgetaway.co.uk/

```html
<!DOCTYPE html>
<html lang="en">
<head>
<meta charset="utf-8">
<title>Bride Basecamp – Hen Day, Night and Weekend Activities</title>
<link rel="stylesheet" href="https://fonts.googleapis.com/css2?family=Open+Sans:wght@400;600;700&family=Varela+Round&display=swap">
<style>
:root{
  --ink:#ffffff;
  --dark:#1c1c1c;
  --dark-2:#242424;
  --band:rgba(12,8,10,.62);
  --yellow:#f6ef1a;
  --orange:#f7941d;
  --orange-dark:#e47c0c;
  --berry:#a33b3b;
  --berry-dark:#8f2f30;
  --field:#f1e3e3;
  --grey:#8b8b8b;
  --grey-light:#dcdcdc;
  --rule:#a8a8a8;
  --text-dark:#333333;
  --text-body:#444444;
  --green:#1f9d3a;
  --muted:#bdbdbd;
}
*{box-sizing:border-box;margin:0;padding:0}
html,body{width:1200px;height:2517px;overflow:hidden;background:var(--dark)}
body{font-family:"Open Sans",Arial,sans-serif;color:var(--ink);position:relative}
.page{position:relative;width:1200px;height:2517px;overflow:hidden}
.abs{position:absolute}
.heading{font-family:"Varela Round","Open Sans",sans-serif}

/* Hero */
.hero{left:0;top:0;width:1200px;height:705px;
  background:
   radial-gradient(ellipse 260px 320px at 1000px 260px,rgba(240,200,170,.55),transparent 70%),
   radial-gradient(ellipse 220px 300px at 680px 330px,rgba(230,190,150,.5),transparent 70%),
   radial-gradient(ellipse 200px 260px at 380px 420px,rgba(200,120,110,.45),transparent 70%),
   radial-gradient(ellipse 500px 400px at 600px 650px,#b0204a,transparent 75%),
   linear-gradient(160deg,#2a0a12 0%,#5a1026 40%,#8e1a3c 70%,#3b0a18 100%)}
.hero-shade{left:0;top:0;width:1200px;height:109px;background:linear-gradient(#0b0507,rgba(11,5,7,.3))}
.social{top:0;display:flex;gap:6px}
.social span{width:24px;height:28px;background:#8d8d8d;clip-path:polygon(0 0,100% 0,100% 100%,50% 80%,0 100%)}
.contact-line{right:200px;font-size:15px;display:flex;align-items:center;gap:7px}
.nav{left:0;top:67px;width:1200px;height:42px;background:rgba(0,0,0,.55)}
.nav-item{top:80px;font-size:13px;letter-spacing:.3px;text-transform:uppercase}
.nav-item.active{top:74px;left:279px;width:125px;height:27px;background:var(--yellow);color:#222;display:flex;align-items:center;justify-content:center}
.search{left:839px;top:72px;width:158px;height:30px;background:#1e1e1e;border:1px solid #444;display:flex;align-items:center;justify-content:space-between;padding:0 10px;font-size:14px}
.brand{left:195px;top:160px;display:flex;align-items:center;gap:10px;font-family:"Varela Round",sans-serif;font-size:38px;color:var(--yellow)}
.brand i{width:22px;height:22px;background:var(--yellow);border-radius:50%}
.network{left:195px;top:235px;width:194px;height:27px;background:rgba(90,90,90,.85);font-size:12px;display:flex;align-items:center;justify-content:center}
.hero-band{left:0;top:514px;width:1200px;height:191px;background:var(--band)}
.hero-title{left:0;top:544px;width:1200px;text-align:center;font-size:25px}
.hero-copy{left:210px;top:588px;width:780px;text-align:center;font-size:13px;line-height:14.5px}
.btn-ribbon{background:var(--orange);color:#fff;display:flex;align-items:center;justify-content:center;clip-path:polygon(0 0,100% 0,94% 50%,100% 100%,0 100%,6% 50%)}
.hero-btn{left:534px;top:648px;width:132px;height:32px;font-size:16px}

/* Locations */
.locations{left:0;top:705px;width:1200px;height:369px;background:#ffffff}
.section-title{color:var(--text-dark);font-size:17px;font-weight:600;width:1200px;text-align:center;left:0;top:768px}
.title-rule{left:357px;top:820px;width:485px;height:3px;background:var(--rule)}
.title-mark{left:593px;top:807px;width:12px;height:26px;background:#777;border-radius:6px}
.loc-card{top:851px;width:158px;height:149px}
.loc-photo{width:158px;height:111px}
.loc-label{height:38px;background:var(--grey);font-size:14px;display:flex;align-items:center;justify-content:center}
.loc-label.current{background:var(--berry)}
.photo-rafting{background:linear-gradient(180deg,#8ab4d8 0%,#3c6a3a 40%,#cfd9df 65%,#2c4a5c 100%)}
.photo-sunset{background:linear-gradient(180deg,#6b2a10 0%,#e07a18 40%,#f6c23a 55%,#c9570f 70%,#3a1606 100%)}
.photo-pier{background:linear-gradient(180deg,#4a5a9a 0%,#b7869c 45%,#e6a58a 60%,#5b4a6a 80%,#2a2a3e 100%)}

/* Dark section */
.dark{left:0;top:1074px;width:1200px;height:1216px;background:
  repeating-linear-gradient(45deg,rgba(255,255,255,.012) 0 2px,transparent 2px 5px),
  linear-gradient(var(--dark),var(--dark-2) 60%,var(--dark))}
.sub-title{font-size:19px;color:#eee}
.video{left:195px;top:1198px;width:468px;height:252px;background:
  linear-gradient(180deg,#e9731f 0%,#d0501a 45%,#7a2a12 75%,#3a1208 100%)}
.play{left:394px;top:1289px;width:68px;height:68px;border-radius:50%;background:rgba(20,20,20,.85);display:flex;align-items:center;justify-content:center}
.caption{left:563px;top:1456px;width:100px;text-align:right;font-size:9px;color:#ccc}
.booking-rule{left:698px;top:1200px;width:309px;height:1px;background:#555}
.booking-copy{left:696px;top:1220px;width:310px;font-size:12.2px;line-height:18px;color:#e5e5e5}
.small-btn{left:695px;top:1425px;width:88px;height:22px;font-size:10px}
.divider{left:0;top:1524px;width:1200px;height:1px;background:#2e2e2e}

/* Form */
.builder{left:309px;top:1587px;width:250px;height:611px;background:var(--berry)}
.panel-title{top:1611px;width:250px;text-align:center;font-size:17px;font-weight:700}
.strap{left:331px;top:1644px;width:206px;height:16px;background:#fff;color:var(--berry);font-size:9.5px;letter-spacing:.4px;display:flex;align-items:center;justify-content:center;clip-path:polygon(0 0,100% 0,97% 50%,100% 100%,0 100%,3% 50%)}
.required{left:329px;top:1687px;font-size:10px;font-style:italic}
.field-label{left:327px;font-size:12px}
.field{left:329px;width:208px;height:22px;background:var(--field);border:1px solid #d9b9b9}
.select-arrow{right:8px;top:4px}
.build-btn{left:332px;top:2128px;width:186px;height:32px;font-size:16px}

/* Reviews */
.reviews{left:591px;top:1587px;width:250px;height:611px;background:#ffffff;color:var(--text-dark)}
.reviews .panel-title{color:#111;font-weight:600}
.badge{left:670px;top:1645px;width:92px;height:15px;background:#4a4a4a;font-size:9.5px;letter-spacing:.5px;display:flex;align-items:center;justify-content:center;clip-path:polygon(0 0,100% 0,94% 50%,100% 100%,0 100%,6% 50%)}
.stars{display:flex;gap:2px}
.star{width:14px;height:14px;background:var(--green);display:flex;align-items:center;justify-content:center}
.count{left:591px;top:1697px;width:250px;text-align:center;font-size:9.5px;color:#555}
.selected{left:591px;top:1723px;width:250px;height:16px;background:var(--grey-light);font-size:10px;font-weight:700;padding-left:16px;display:flex;align-items:center;color:#222}
.review{left:606px;width:222px;height:148px}
.review .date{position:absolute;right:2px;top:0;font-size:9.5px;font-style:italic}
.review .stars .star{width:9px;height:9px}
.review .headline{position:absolute;top:19px;left:0;font-size:8.5px;display:flex;align-items:center;gap:4px}
.review .headline b{display:inline-block;width:66px;height:5px;background:#bbb}
.review p{position:absolute;top:32px;left:0;font-size:9.4px;line-height:14px;color:var(--text-body)}
.review p span{color:var(--orange-dark)}
.review .author{position:absolute;top:78px;left:0;font-size:9.5px;font-style:italic;display:flex;align-items:center;gap:5px}
.review-rule{left:591px;width:250px;height:1px;background:#ddd}
.reviews-foot{left:591px;top:2181px;width:250px;height:17px;background:var(--grey-light);font-size:8.5px;font-weight:700;display:flex;align-items:center;gap:4px;padding-left:6px;color:#222}

/* Footer */
.footer-rule{left:0;top:2290px;width:1200px;height:1px;background:#333}
.footer-social{left:560px;top:2296px;display:flex;gap:7px}
.footer-social span{width:24px;height:30px;background:#777}
.footer-line{left:0;width:1200px;text-align:center;font-size:11px;color:#ddd}
.call{top:2350px;font-size:18px;font-weight:700;color:#fff}
</style>
</head>
<body>
<div class="page">

  <!-- Hero -->
  <div class="abs hero" role="img" aria-label="Photo of friends dancing and celebrating at a hen night under disco lights"></div>
  <div class="abs hero-shade"></div>
  <div class="abs social" style="left:195px"><span></span><span></span><span></span></div>
  <div class="abs contact-line" style="top:12px">
    <svg width="12" height="13" viewBox="0 0 24 24"><path fill="#fff" d="M6.6 10.8a15.1 15.1 0 0 0 6.6 6.6l2.2-2.2c.3-.3.7-.4 1-.2 1.1.4 2.3.6 3.6.6.6 0 1 .4 1 1V20c0 .6-.4 1-1 1A17 17 0 0 1 3 4c0-.6.4-1 1-1h3.5c.6 0 1 .4 1 1 0 1.3.2 2.5.6 3.6.1.3 0 .7-.2 1z"/></svg>
    Call 0131 555 0192
  </div>
  <div class="abs contact-line" style="top:31px">
    <svg width="14" height="10" viewBox="0 0 14 10"><rect x=".5" y=".5" width="13" height="9" fill="none" stroke="#fff"/><path d="M.5.5 7 6l6.5-5.5" fill="none" stroke="#fff"/></svg>
    info@bridebasecamp.co.uk
  </div>

  <nav class="abs nav" aria-label="Main"></nav>
  <div class="abs nav-item" style="left:195px">Home</div>
  <div class="abs nav-item active">Locations</div>
  <div class="abs nav-item" style="left:445px">European Destinations</div>
  <div class="abs nav-item" style="left:681px">Contact</div>
  <div class="abs search"><span>Search</span>
    <svg width="12" height="12" viewBox="0 0 12 12"><circle cx="5" cy="5" r="3.6" fill="none" stroke="#fff" stroke-width="1.6"/><path d="M7.6 7.6 11 11" stroke="#fff" stroke-width="1.8"/></svg>
  </div>

  <div class="abs brand"><i></i>PartyPeel</div>
  <div class="abs network">Part of the PartyPeel Network</div>

  <div class="abs hero-band"></div>
  <h1 class="abs hero-title heading">Bride Basecamp - Hen Day, Night and Weekend Activities</h1>
  <p class="abs hero-copy">Bride Basecamp is the place to start if you want to put together a great hen party. We have done 1000's of them over the years and know all the great places and things to do. Rather than build a big site with loads of pages that you will never read we decided lets cut to the chase and make it easy for you. All you have to do is fill out our form below and we will create a great itinerary for you.</p>
  <div class="abs btn-ribbon hero-btn">Learn More</div>

  <!-- Locations -->
  <section class="abs locations"></section>
  <h2 class="abs section-title heading">Hen Day-Night Activities, Locations</h2>
  <div class="abs title-rule"></div>
  <div class="abs title-mark"></div>

  <div class="abs loc-card" style="left:195px"><div class="loc-photo photo-rafting" role="img" aria-label="White water rafting on a river"></div><div class="loc-label">Aviemore</div></div>
  <div class="abs loc-card" style="left:357px"><div class="loc-photo photo-sunset" role="img" aria-label="Sunset over the sea"></div><div class="loc-label current">Bournemouth</div></div>
  <div class="abs loc-card" style="left:520px"><div class="loc-photo photo-rafting" role="img" aria-label="White water rafting on a river"></div><div class="loc-label">Aviemore</div></div>
  <div class="abs loc-card" style="left:683px"><div class="loc-photo photo-sunset" role="img" aria-label="Sunset over the sea"></div><div class="loc-label">Bournemouth</div></div>
  <div class="abs loc-card" style="left:847px"><div class="loc-photo photo-pier" role="img" aria-label="Seaside pier at dusk"></div><div class="loc-label">Brighton</div></div>

  <!-- What we do -->
  <section class="abs dark"></section>
  <h2 class="abs sub-title heading" style="left:195px;top:1163px">What We Do?</h2>
  <div class="abs video" role="img" aria-label="Video still of a cartoon mascot in front of an orange sunset"></div>
  <div class="abs play"><svg width="26" height="30" viewBox="0 0 26 30"><path d="M3 2v26l21-13z" fill="#fff"/></svg></div>
  <div class="abs caption">Click to Large</div>

  <h2 class="abs sub-title heading" style="left:698px;top:1163px">Booking Your Hen</h2>
  <div class="abs booking-rule"></div>
  <p class="abs booking-copy">Lorem ipsum dolor sit amet, consectetur adipiscing elit. In fermentum dolor non augue pretium egestas. Donec sem eros, tincidunt at congue ut, posuere sit amet est. Vivamus scelerisque viverra odio sit amet laoreet. Ut nec neque non justo rutrum tempor lobortis eu ante. Aliquam sagittis, nibh quis commodo auctor, risus mauris laoreet lectus, id facilisis libero odio nec enim. Sed id ligula adipiscing purus lacinia aliquet. Sed eu est non nisl vehicula bibendum congue sit amet enim.</p>
  <div class="abs btn-ribbon small-btn">Learn More</div>

  <div class="abs divider"></div>

  <!-- Package builder -->
  <form class="abs builder" aria-label="Hen Package Builder"></form>
  <h3 class="abs panel-title heading" style="left:309px">Hen Package Builder</h3>
  <div class="abs strap">TAKES LESS THAN 2 MINUTES</div>
  <div class="abs required">* required fields</div>

  <label class="abs field-label" style="top:1725px">First Name *</label><div class="abs field" style="top:1745px"></div>
  <label class="abs field-label" style="top:1778px">Surname *</label><div class="abs field" style="top:1798px"></div>
  <label class="abs field-label" style="top:1832px">Tel Number *</label><div class="abs field" style="top:1852px"></div>
  <label class="abs field-label" style="top:1885px">Email *</label><div class="abs field" style="top:1905px"></div>
  <label class="abs field-label" style="top:1945px">Choose Your Date *</label><div class="abs field" style="top:1965px"></div>
  <label class="abs field-label" style="top:2000px">How Many People?</label><div class="abs field" style="top:2020px"></div>
  <label class="abs field-label" style="top:2057px">Choose Your Location*</label>
  <div class="abs field" style="top:2077px"><svg class="abs select-arrow" width="12" height="12" viewBox="0 0 12 12"><path d="M2 4l4 4 4-4" fill="none" stroke="#555" stroke-width="1.6"/></svg></div>
  <div class="abs btn-ribbon build-btn">Build Your Party</div>

  <!-- Reviews -->
  <aside class="abs reviews"></aside>
  <h3 class="abs panel-title heading" style="left:591px;color:#111">Customer Reviews</h3>
  <div class="abs badge">EXCELLENT</div>
  <div class="abs stars" style="left:672px;top:1666px">
    <span class="star"><svg width="10" height="10" viewBox="0 0 10 10"><path d="M5 .6l1.3 3h3.2L7 5.5l1 3.2L5 6.8 2 8.7l1-3.2L.5 3.6h3.2z" fill="#fff"/></svg></span>
    <span class="star"><svg width="10" height="10" viewBox="0 0 10 10"><path d="M5 .6l1.3 3h3.2L7 5.5l1 3.2L5 6.8 2 8.7l1-3.2L.5 3.6h3.2z" fill="#fff"/></svg></span>
    <span class="star"><svg width="10" height="10" viewBox="0 0 10 10"><path d="M5 .6l1.3 3h3.2L7 5.5l1 3.2L5 6.8 2 8.7l1-3.2L.5 3.6h3.2z" fill="#fff"/></svg></span>
    <span class="star"><svg width="10" height="10" viewBox="0 0 10 10"><path d="M5 .6l1.3 3h3.2L7 5.5l1 3.2L5 6.8 2 8.7l1-3.2L.5 3.6h3.2z" fill="#fff"/></svg></span>
    <span class="star"><svg width="10" height="10" viewBox="0 0 10 10"><path d="M5 .6l1.3 3h3.2L7 5.5l1 3.2L5 6.8 2 8.7l1-3.2L.5 3.6h3.2z" fill="#fff"/></svg></span>
  </div>
  <div class="abs count">72 customer have written a review on ReviewStar</div>
  <div class="abs selected">Selected Review</div>

  <div class="abs review" style="top:1755px">
    <div class="stars"><span class="star"></span><span class="star"></span><span class="star"></span><span class="star"></span><span class="star"></span></div>
    <span class="date">06 March</span>
    <div class="headline">EXCELLENT <b></b></div>
    <p>Lorem ipsum dolor sit amet consec tetur adipisci<br>cing elit, do eiusmod &nbsp;consecad pisicing sit amet<br>consec.. <span>Read More</span></p>
    <div class="author"><svg width="12" height="12" viewBox="0 0 12 12"><circle cx="6" cy="4" r="3" fill="#aaa"/><path d="M0 12a6 5 0 0 1 12 0z" fill="#aaa"/></svg>Morag</div>
  </div>
  <div class="abs review-rule" style="top:1885px"></div>

  <div class="abs review" style="top:1905px">
    <div class="stars"><span class="star"></span><span class="star"></span><span class="star"></span><span class="star"></span><span class="star"></span></div>
    <span class="date">06 March</span>
    <div class="headline">EXCELLENT <b></b></div>
    <p>Lorem ipsum dolor sit amet consec tetur adipisci<br>cing elit, do eiusmod &nbsp;consecad pisicing sit amet<br>consec.. <span>Read More</span></p>
    <div class="author"><svg width="12" height="12" viewBox="0 0 12 12"><circle cx="6" cy="4" r="3" fill="#aaa"/><path d="M0 12a6 5 0 0 1 12 0z" fill="#aaa"/></svg>Morag</div>
  </div>
  <div class="abs review-rule" style="top:2031px"></div>

  <div class="abs review" style="top:2051px">
    <div class="stars"><span class="star"></span><span class="star"></span><span class="star"></span><span class="star"></span><span class="star"></span></div>
    <span class="date">06 March</span>
    <div class="headline">EXCELLENT <b></b></div>
    <p>Lorem ipsum dolor sit amet consec tetur adipisci<br>cing elit, do eiusmod &nbsp;consecad pisicing sit amet<br>consec.. <span>Read More</span></p>
    <div class="author"><svg width="12" height="12" viewBox="0 0 12 12"><circle cx="6" cy="4" r="3" fill="#aaa"/><path d="M0 12a6 5 0 0 1 12 0z" fill="#aaa"/></svg>Morag</div>
  </div>
  <div class="abs reviews-foot">REVIEWSTAR</div>

  <!-- Footer -->
  <div class="abs footer-rule"></div>
  <div class="abs footer-social"><span></span><span></span><span></span></div>
  <div class="abs footer-line call">Call us on 0131 555 0192</div>
  <div class="abs footer-line" style="top:2384px">Copyright 2014 - PartyPeel. All rights reserved</div>
  <div class="abs footer-line" style="top:2403px">Operated Under Registration No: SC482907 by PlanAhead Events Ltd, 14 Market Lane, Blairgowrie, Perthshire, PH10 2XY</div>
  <div class="abs footer-line" style="top:2422px">About Us | SiteMap | Terms and Conditions</div>

</div>
</body>
</html>
```